Letterhead Design Project

I am the new owner of an existing Accouting and Financial Planning Firm (which I have been an employee at for 3 years)
We need to change the letterhead due to a change to the company's ABN etc., so thought we would like to modernise this at the same time.
We wish to keep the existing logo so there is familiarity to the clients. As per the notes on the attached document, we are happy to remove the wording from the logo, whichever will look better.
The letterhead needs to be professional, yet modern.
I will upload our logo and the required details for the letterhead.

Industry/Entity Type

Financial

Requirements
Must have
• Logo and provided business details.

```html
<!DOCTYPE html>
<html lang="en">
<head>
<meta charset="utf-8">
<title>Kestrel Accountants – Letterhead</title>
<link rel="stylesheet" href="https://fonts.googleapis.com/css2?family=Open+Sans:wght@400;700&display=swap">
<style>
  :root {
    --navy: #0f3d7c;
    --ink: #1f4a86;
    --mist: #d6e0ea;
    --cream: #fbeed6;
    --paper: #ffffff;
    --edge: #333333;
  }
  * { margin: 0; padding: 0; box-sizing: border-box; }
  html, body {
    width: 1200px; height: 900px; overflow: hidden;
    background: var(--paper);
    font-family: "Open Sans", Arial, sans-serif;
  }
  .canvas { position: relative; width: 1200px; height: 900px; }
  .sheet {
    position: absolute; top: 62px; width: 528px; height: 747px;
    border: 1px solid var(--edge); background: var(--paper); overflow: hidden;
  }
  .sheet--primary { left: 47px; }
  .sheet--continuation { left: 619px; }

  .backdrop { position: absolute; top: 0; left: 0; }

  .brand {
    position: absolute; display: flex; align-items: center; gap: 6px;
    color: var(--navy); font-weight: 700; letter-spacing: 0.02em;
    text-transform: uppercase; line-height: 1;
  }
  .brand__mark { background: var(--navy); display: block; }
  .sheet--primary .brand { top: 40px; left: 53px; font-size: 22px; }
  .sheet--primary .brand__mark { width: 16px; height: 16px; }
  .sheet--continuation .brand { top: 40px; right: 30px; font-size: 14px; }
  .sheet--continuation .brand__mark { width: 11px; height: 11px; }

  .footer {
    position: absolute; left: 32px; right: 31px;
    display: flex; justify-content: space-between; align-items: flex-end;
    color: var(--ink); text-transform: uppercase; white-space: nowrap;
  }
  .footer address { font-style: normal; }
  .footer__contact { text-align: right; }
  .footer__contact .gap { margin-top: var(--gap, 0); }

  .sheet--primary .footer { bottom: 28px; font-size: 9.4px; line-height: 12.5px; }
  .sheet--continuation .footer { bottom: 33px; font-size: 7.2px; line-height: 10.1px; }
  .sheet--continuation .footer__contact { --gap: 10.1px; }
</style>
</head>
<body>
<main class="canvas">

  <section class="sheet sheet--primary" aria-label="Letterhead, first page">
    <svg class="backdrop" width="528" height="300" viewBox="0 0 528 300" role="img" aria-label="Soft blue panel with a pale cream diagonal band">
      <defs>
        <linearGradient id="mistFade" x1="0" y1="0" x2="1" y2="1">
          <stop offset="0" stop-color="var(--mist)"/>
          <stop offset="1" stop-color="var(--mist)" stop-opacity="0.35"/>
        </linearGradient>
      </defs>
      <rect x="0" y="0" width="260" height="236" fill="url(#mistFade)"/>
      <path d="M200 236 L 400 20 L 430 20 L 230 236 Z" fill="var(--cream)"/>
    </svg>
    <div class="brand"><span class="brand__mark"></span>Kestrel</div>
    <footer class="footer">
      <address>
        <p>Kestrel Accountants &amp; Financial Services</p>
        <p>12 Harlow Street, Riverton, VIC, 3700,</p>
        <p>PO Box 5580, Brookvale, NSW, 2650</p>
      </address>
      <div class="footer__contact">
        <p>ABN: 00 123 456 789</p>
        <p>PH: 02 5550 1234</p>
        <p>FAX: 02 5550 5678</p>
        <p>Email: admin@kestrelaccountants.com.au</p>
        <p>www.kestrelaccountants.com.au</p>
      </div>
    </footer>
  </section>

  <section class="sheet sheet--continuation" aria-label="Letterhead, following pages">
    <svg class="backdrop" width="528" height="330" viewBox="0 0 528 330" role="img" aria-label="Pale cream diagonal band across the top corner">
      <path d="M70 0 L 320 0 L 0 322 L 0 70 Z" fill="var(--cream)"/>
    </svg>
    <div class="brand"><span class="brand__mark"></span>Kestrel</div>
    <footer class="footer">
      <address>
        <p>Kestrel Accountants</p>
        <p>&nbsp;&amp; Financial Services</p>
        <p>12 Harlow Street,</p>
        <p>Riverton, VIC, 3700,</p>
        <p>PO Box 5580,</p>
        <p>Brookvale, NSW, 2650</p>
      </address>
      <div class="footer__contact">
        <p>ABN: 00 123 456 789</p>
        <p>PH: 02 5550 1234</p>
        <p>FAX: 02 5550 5678</p>
        <p class="gap">Email: admin@kestrelaccountants.com.au</p>
        <p>www.kestrelaccountants.com.au</p>
      </div>
    </footer>
  </section>

</main>
</body>
</html>
```